Running Book Cover Design Project

My client has written a book about running and his accomplishments throughout the sport, his story etc. We need to get a cover designed for it. The book will be offered online only, but may later on look at printing a few copies later down the track, so it will need to be a vector graphic so we can resize it easily.

The title of the book is 'Beyond The Far Hill', written by Marco Tevin Alcaraza from the Philippines.

The idea that we have had for the cover is as follows... We would like the word 'step' so be somehow presented in a step, maybe we could use the shoe tread somehow with the word step in it, or use a step in some way, I will leave it up to you, we are pretty open.

Just think that finding running has changed his life and he wants that represented on the cover somehow with the title standing for both taking one more step with running and a metaphor for life.

Do note that the illustration of the 'foot step' has to be a mid-foot or forefoot landing on the ground instead of a heel strike. Reason being that heel strikes can lead to a lot of injuries; the author is against it as well.

UPDATE: The design should have the runner in summer clothes, with bold fonts, not running up steps as these are marathon type events he is running (attached a new image for inspiration), he should be wearing shoes and clothing similar to the attached images from Talvex
Updates

Changes:

AUTHOR - Colin Barr

Sorry about the inclusion of Marco, the author's name should be represented as Colin Barr

Still waiting on final approval, apologies!

Target Market(s)

Adults based in south east asia predominantly singapore and the philippines.

Targeted to all those who enjoy inspirational stories or books about running

Industry/Entity Type

Printing

Requirements
Must have
• Running imagery
Shoe/Step IIllustration
Title of Book
Author's Name

```html
<!DOCTYPE html>
<html lang="en">
<head>
<meta charset="utf-8">
<title>Beyond The Far Hill — Book Cover</title>
<link rel="stylesheet" href="https://fonts.googleapis.com/css2?family=Tenor+Sans&display=swap">
<style>
  :root {
    --page-bg: #ffffff;
    --cover-border: #4a4a4a;
    --sky-top: #a7bbcc;
    --sky-bottom: #eaf0f4;
    --ground-top: #e4e0da;
    --ground-bottom: #cfcac3;
    --horizon: #2e2e2e;
    --title-light: #9fb4c6;
    --title-mid: #5f7c95;
    --title-dark: #3a566e;
    --title-outline: #ffffff;
    --author-ink: #4f4f4f;
    --runner-tone: #2a2a2a;
    --shadow-tone: #8e959b;
  }
  * { margin: 0; padding: 0; box-sizing: border-box; }
  html, body {
    width: 1200px;
    height: 900px;
    overflow: hidden;
    background: var(--page-bg);
  }
  .canvas {
    position: relative;
    width: 1200px;
    height: 900px;
  }
  .book-cover {
    position: absolute;
    left: 315px;
    top: 15px;
    width: 573px;
    height: 864px;
    border: 1.5px solid var(--cover-border);
    overflow: hidden;
  }
  .book-cover svg { display: block; }
  .title-line {
    font-family: "Tenor Sans", "Optima", sans-serif;
    text-anchor: middle;
    fill: url(#titleFill);
    stroke: var(--title-outline);
    stroke-width: 3.5;
    paint-order: stroke;
    filter: url(#titleShadow);
  }
  .author-name {
    font-family: "Tenor Sans", "Optima", sans-serif;
    font-size: 34px;
    fill: var(--author-ink);
    text-anchor: middle;
  }
</style>
</head>
<body>
<main class="canvas">
  <section class="book-cover" aria-label="Book cover: Beyond The Far Hill by Colin Barr">
    <svg width="573" height="864" viewBox="0 0 573 864" xmlns="http://www.w3.org/2000/svg">
      <defs>
        <linearGradient id="skyFill" x1="0" y1="0" x2="0" y2="1">
          <stop offset="0" stop-color="var(--sky-top)"/>
          <stop offset="1" stop-color="var(--sky-bottom)"/>
        </linearGradient>
        <linearGradient id="groundFill" x1="0" y1="0" x2="0" y2="1">
          <stop offset="0" stop-color="var(--ground-top)"/>
          <stop offset="1" stop-color="var(--ground-bottom)"/>
        </linearGradient>
        <linearGradient id="titleFill" x1="0" y1="0" x2="0" y2="1">
          <stop offset="0" stop-color="var(--title-light)"/>
          <stop offset="0.5" stop-color="var(--title-mid)"/>
          <stop offset="1" stop-color="var(--title-dark)"/>
        </linearGradient>
        <linearGradient id="castShadowFill" x1="1" y1="0" x2="0" y2="1">
          <stop offset="0" stop-color="var(--shadow-tone)" stop-opacity="0.75"/>
          <stop offset="1" stop-color="var(--shadow-tone)" stop-opacity="0.1"/>
        </linearGradient>
        <filter id="titleShadow" x="-10%" y="-10%" width="120%" height="130%">
          <feDropShadow dx="2" dy="4" stdDeviation="3" flood-color="#000" flood-opacity="0.3"/>
        </filter>
      </defs>

      <!-- sky band -->
      <rect class="sky" x="0" y="0" width="573" height="180" fill="url(#skyFill)"/>
      <!-- ground plane -->
      <rect class="ground" x="0" y="180" width="573" height="684" fill="url(#groundFill)"/>
      <!-- horizon edge -->
      <rect class="horizon" x="0" y="178" width="573" height="4" fill="var(--horizon)"/>
      <rect x="0" y="182" width="573" height="6" fill="#000" opacity="0.08"/>

      <!-- runner's long cast shadow -->
      <polygon class="runner-shadow" role="img" aria-label="Long cast shadow of the runner stretching down the ground"
        points="430,185 470,185 400,330 300,520 190,700 150,690 250,500 350,320"
        fill="url(#castShadowFill)"/>

      <!-- runner illustration area -->
      <rect class="runner-figure" role="img" aria-label="Silhouette of a runner in summer running kit striding along the horizon edge"
        x="425" y="10" width="85" height="168" rx="20" fill="var(--runner-tone)" opacity="0.85"/>

      <!-- title -->
      <text class="title-line" x="287" y="345" font-size="104" textLength="330" lengthAdjust="spacingAndGlyphs">BEYOND</text>
      <text class="title-line" x="287" y="487" font-size="148">THE</text>
      <text class="title-line" x="287" y="600" font-size="120">FAR</text>
      <text class="title-line" x="287" y="735" font-size="148">HILL</text>

      <!-- author -->
      <text class="author-name" x="287" y="815">Colin Barr</text>
    </svg>
  </section>
</main>
</body>
</html>
```